Membership card design for video game arena

I need a two sided design for membership cards for my customers. It needs to have instructions on how to book on one side, and a nice catchy design for the other.

Please pull logo and whatever you desire from the website www.vornik-play.com

Industry/Entity Type

Entertainment

Contact Information for Business Card

The front must say Vornik-Play with the address and whatever design you choose. The back must have the details below

Colors

Designer to choose colors to be used in the design.

Requirements
Must have
• Frontside
• Company name address and phone number
• Backside
• Booking Instructions
• www.Vornik-Play.com/book-now
• Click on General Admission and input information
• Use code Gatepass7 to gain access
• See you there!
Nice to have
• A nice design and whatever you find is pertinent
Should not have
• Useless info

```html
<!DOCTYPE html>
<html lang="en">
<head>
<meta charset="utf-8">
<title>Vornik-Play Membership Card</title>
<link rel="stylesheet" href="https://fonts.googleapis.com/css2?family=Montserrat:ital,wght@0,300;0,400;0,600;0,700;1,800&display=swap">
<style>
  :root {
    --page-bg: #e4e1dc;
    --card-bg: #333335;
    --accent: #f6b21b;
    --text-light: #f2f2f2;
    --text-soft: #d9d9d9;
    --mark-grey: #bdbdbd;
    --mark-dark: #121212;
  }
  * { margin: 0; padding: 0; box-sizing: border-box; }
  html, body {
    width: 1063px; height: 1200px; overflow: hidden;
    background: var(--page-bg);
    font-family: "Montserrat", Arial, sans-serif;
  }
  .canvas { position: relative; width: 1063px; height: 1200px; }
  .card {
    position: absolute; left: 100px; width: 850px; height: 485px;
    background: var(--card-bg); color: var(--text-light);
  }
  .card--front { top: 94px; }
  .card--back { top: 615px; }

  /* Front */
  .brand-dot {
    position: absolute; border-radius: 50%;
  }
  .card--front .brand-dot {
    left: 164px; top: 173px; width: 100px; height: 100px;
    background: var(--mark-grey);
  }
  .brand-name {
    position: absolute; font-weight: 700; letter-spacing: 2px; white-space: nowrap;
  }
  .card--front .brand-name {
    left: 65px; top: 287px; width: 298px; text-align: center;
    font-size: 29px; color: var(--text-light);
  }
  .divider {
    position: absolute; left: 424px; top: 163px; width: 2px; height: 169px;
    background: var(--accent);
  }
  .holder { position: absolute; left: 482px; top: 158px; }
  .holder__name { font-size: 25px; font-weight: 600; color: var(--accent); letter-spacing: 0.5px; line-height: 30px; }
  .holder__role { font-size: 21px; font-weight: 300; color: var(--text-soft); letter-spacing: 1px; line-height: 28px; }
  .contact-list { position: absolute; left: 482px; top: 237px; list-style: none; }
  .contact-list li {
    display: flex; align-items: center; height: 31.5px;
    font-size: 22.5px; font-weight: 300; color: var(--text-soft); letter-spacing: 0.5px;
  }
  .contact-list svg { width: 22px; height: 22px; margin-right: 20px; flex: none; }
  .address {
    position: absolute; left: 164px; top: 386px; display: flex; align-items: center;
    font-size: 22.5px; font-weight: 300; color: var(--text-soft); letter-spacing: 1px;
  }
  .address svg { width: 28px; height: 32px; margin-right: 12px; }

  /* Back */
  .card--back .brand-dot {
    left: 353px; top: 44px; width: 106px; height: 106px;
    background: var(--mark-dark);
  }
  .card--back .brand-name {
    left: 0; width: 850px; top: 158px; text-align: center;
    font-size: 30px; color: var(--mark-dark);
  }
  .booking-title {
    position: absolute; left: 0; width: 870px; top: 225px; text-align: center;
    font-size: 26px; font-weight: 600; letter-spacing: 1.5px;
    text-decoration: underline; text-decoration-thickness: 2px; text-underline-offset: 5px;
  }
  .steps { position: absolute; left: 0; top: 290px; width: 850px; list-style: none; }
  .steps li {
    display: flex; justify-content: center; align-items: center; height: 38px;
    font-size: 22.5px; font-weight: 300; letter-spacing: 1px; color: var(--text-soft);
  }
  .step-marker { width: 30px; height: 30px; margin-right: 14px; flex: none; }
  .sign-off {
    position: absolute; right: 45px; top: 430px;
    font-size: 22.5px; font-weight: 800; font-style: italic; letter-spacing: 1px;
  }
</style>
</head>
<body>
<main class="canvas">
  <section class="card card--front" aria-label="Card front">
    <div class="brand-dot"></div>
    <div class="brand-name">VORNIK-PLAY</div>
    <div class="divider"></div>
    <div class="holder">
      <div class="holder__name">DANA WHITLOCK</div>
      <div class="holder__role">OWNER</div>
    </div>
    <ul class="contact-list">
      <li>
        <svg viewBox="0 0 24 24" aria-hidden="true"><path fill="#f6b21b" d="M6.6 10.8c1.4 2.8 3.8 5.1 6.6 6.6l2.2-2.2c.3-.3.7-.4 1-.2 1.1.4 2.3.6 3.6.6.6 0 1 .4 1 1V20c0 .6-.4 1-1 1C10.6 21 3 13.4 3 4c0-.6.4-1 1-1h3.5c.6 0 1 .4 1 1 0 1.3.2 2.5.6 3.6.1.3 0 .7-.2 1l-2.3 2.2z"/></svg>
        555.014.2290
      </li>
      <li>
        <svg viewBox="0 0 24 24" aria-hidden="true"><rect x="2" y="5" width="20" height="14" fill="#f6b21b"/><path d="M2 5l10 8 10-8" fill="none" stroke="#333335" stroke-width="1.6"/><path d="M2 19l7-6M22 19l-7-6" stroke="#333335" stroke-width="1.2"/></svg>
        dana@vornik-play.com
      </li>
      <li>
        <svg viewBox="0 0 24 24" aria-hidden="true"><circle cx="12" cy="12" r="10" fill="#f6b21b"/><g fill="none" stroke="#333335" stroke-width="1.2"><ellipse cx="12" cy="12" rx="4.5" ry="10"/><path d="M12 2v20M2 12h20M4 7h16M4 17h16"/></g></svg>
        www.Vornik-Play.com
      </li>
    </ul>
    <div class="address">
      <svg viewBox="0 0 28 32" aria-hidden="true"><path fill="#f6b21b" d="M14 1C8.5 1 5 5 5 10c0 6.5 9 15 9 15s9-8.5 9-15c0-5-3.5-9-9-9z"/><circle cx="14" cy="10" r="3.5" fill="#333335"/><ellipse cx="14" cy="27" rx="11" ry="4" fill="none" stroke="#f6b21b" stroke-width="1.5"/></svg>
      2710 W HARBOR LN, LAKEVIEW FL 33990
    </div>
  </section>

  <section class="card card--back" aria-label="Card back">
    <div class="brand-dot"></div>
    <div class="brand-name">VORNIK-PLAY</div>
    <h2 class="booking-title">BOOKING INSTRUCTIONS</h2>
    <ol class="steps">
      <li>
        <svg class="step-marker" viewBox="0 0 30 30" aria-hidden="true"><path d="M1 0L29 15L1 30z" fill="#fff"/><text x="4" y="21" font-family="Montserrat, Arial, sans-serif" font-size="17" font-weight="700" fill="#222">1</text></svg>
        WWW.VORNIK-PLAY.COM/BOOK-NOW
      </li>
      <li>
        <svg class="step-marker" viewBox="0 0 30 30" aria-hidden="true"><path d="M1 0L29 15L1 30z" fill="#fff"/><text x="3" y="21" font-family="Montserrat, Arial, sans-serif" font-size="17" font-weight="700" fill="#222">2</text></svg>
        CLICK ON GENERAL ADMISSION AND INPUT INFORMATION
      </li>
      <li>
        <svg class="step-marker" viewBox="0 0 30 30" aria-hidden="true"><path d="M1 0L29 15L1 30z" fill="#fff"/><text x="3" y="21" font-family="Montserrat, Arial, sans-serif" font-size="17" font-weight="700" fill="#222">3</text></svg>
        USE CODE GATEPASS7 TO GAIN ACCESS
      </li>
    </ol>
    <p class="sign-off">SEE YOU THERE!</p>
  </section>
</main>
</body>
</html>
```